Full web page for optical stores company

We need a company website design for optical stores company. We have stores in differnt cities and our main products: glasses frames, glasses lenses, contact lenses, sun glasses.
We would like a website design that use our brandbook directions.

All needed page wireframes, previews with comments are provided, also brandbook and other materials are included.

We need design for all pages (10 wireframes). .PSD files will be necessary.
At first only title page and one subpage design can be provided for our evaluation.

Wireframes links (for quick preview):
Title: http://mockvane.com/app/viewer.php?k=a81f09c3e27b4d6f8a05c9e1b3d74f2e&pr=583902&pg=583902_1_3&a=347058&sitemap=false

Title with top menu: http://mockvane.com/app/viewer.php?k=c4e7a90b12f3486d9e21b07a5c6d38f1&pr=590317&pg=590317_9&a=352961&sitemap=false

Discounts: http://mockvane.com/app/viewer.php?k=f0b93d6e48a1c27e5d09b4f8a3e61c7d&pr=583902&pg=583902_1_3_6_14&a=347058&sitemap=false

Products: http://mockvane.com/app/viewer.php?k=2b7e05f1c9a34d86b1e0f7a29c58d3e4&pr=583902&pg=583902_1_3_6_14_22&a=347058&sitemap=false

Products big photo: http://mockvane.com/app/viewer.php?k=8d3c61a0f5e2479b0c8a1d5e6f27b9c3&pr=590317&pg=590317_13&a=352961&sitemap=false

Articles list: http://mockvane.com/app/viewer.php?k=5a0f84e2b7d1c39e6f58a0b3d2c7e41f&pr=583902&pg=583902_1_3_6_14_16&a=347058&sitemap=false

Article: http://mockvane.com/app/viewer.php?k=9f1d2c7a08e6b54f3a1c9e0d7b48f26a&pr=590317&pg=590317_2_7&a=352961&sitemap=false

Optician registration: http://mockvane.com/app/viewer.php?k=3e8b0a5f6c21d97e4b0f3a8c1d6e52b9&pr=583902&pg=583902_1_3_6_14_16_18&a=347058&sitemap=false

Optician calendar: http://mockvane.com/app/viewer.php?k=b06c9e3d1f48a27e5c0d9b3a6f1e84c2&pr=590317&pg=590317_11&a=352961&sitemap=false

Contacts: http://mockvane.com/app/viewer.php?k=61a2e8f0c7d35b94e1f6a0c8b3d29e7a&pr=590317&pg=590317_2&a=352961&sitemap=false

```html
<!DOCTYPE html>
<html lang="en">
<head>
<meta charset="utf-8">
<title>Lumora – Featurez</title>
<link rel="stylesheet" href="https://fonts.googleapis.com/css2?family=Ubuntu:wght@400;500;700&display=swap">
<style>
  :root {
    --header-dark: #1f1a17;
    --nav-dark: #2c2a29;
    --footer-dark: #232222;
    --bottom-bar: #151515;
    --accent-red: #e03a22;
    --accent-orange: #f0a11c;
    --soft-pink: #f27a7a;
    --panel-grey: #ebebeb;
    --menu-grey: #e2e2e2;
    --rule-grey: #c9c9c9;
    --text-body: #4a4a4a;
    --text-dark: #2e2e2e;
    --white: #ffffff;
  }
  * { box-sizing: border-box; margin: 0; padding: 0; }
  html, body { width: 1028px; height: 1200px; overflow: hidden; }
  body {
    position: relative;
    background: var(--white);
    font-family: "Ubuntu", Arial, sans-serif;
    color: var(--text-body);
  }
  a { color: inherit; text-decoration: none; }

  /* Header */
  .site-header {
    position: absolute; left: 0; top: 0; width: 1028px; height: 94px;
    background: var(--header-dark);
    border-bottom: 2px solid var(--accent-orange);
  }
  .brand {
    position: absolute; left: 139px; top: 18px;
    font-size: 46px; font-weight: 700; color: var(--white); letter-spacing: -1px;
  }
  .member-label {
    position: absolute; left: 281px; top: 50px;
    font-size: 6px; color: var(--accent-orange);
  }
  .partner-divider {
    position: absolute; left: 314px; top: 26px; width: 2px; height: 40px;
    background: var(--accent-orange);
  }
  .partner-badge {
    position: absolute; left: 330px; top: 28px; width: 102px; height: 36px;
    background: #3a3330; border-radius: 3px;
  }
  .utility-links {
    position: absolute; right: 138px; top: 8px;
    font-size: 8px; color: var(--white);
  }
  .utility-links span { margin: 0 3px; }
  .social { position: absolute; right: 138px; top: 24px; display: flex; gap: 3px; }
  .social i { display: block; width: 22px; height: 22px; border-radius: 50%; }
  .social .s-red { background: #dd4b39; }
  .social .s-blue { background: #3b63b0; }

  /* Nav */
  .main-nav {
    position: absolute; left: 0; top: 96px; width: 1028px; height: 30px;
    background: var(--nav-dark);
  }
  .nav-links {
    position: absolute; left: 144px; top: 0; height: 30px;
    display: flex; align-items: center;
    font-size: 10px; color: var(--white); text-transform: uppercase;
  }
  .nav-links li { list-style: none; padding: 0 12px; border-left: 2px solid var(--accent-red); line-height: 14px; }
  .nav-links li:first-child { padding-left: 0; border-left: 0; }
  .nav-cta { position: absolute; top: 3px; height: 24px; }
  .nav-cta .cta-bg { position: absolute; inset: 0; background: var(--accent-red); transform: skewX(-18deg); }
  .nav-cta .cta-text {
    position: relative; display: flex; align-items: center; justify-content: center; gap: 8px;
    height: 24px; font-size: 10.5px; color: var(--white);
  }
  .cta-optician { left: 630px; width: 112px; }
  .cta-shop { left: 742px; width: 140px; }

  /* Breadcrumb panel */
  .category-panel {
    position: absolute; left: 137px; top: 165px; width: 754px; height: 70px;
    background: var(--panel-grey);
  }
  .category-panel h2 {
    position: absolute; left: 13px; top: 7px; right: 10px;
    font-size: 13px; font-weight: 400; color: var(--accent-red);
    padding-bottom: 9px; border-bottom: 1px solid #b9b9b9;
  }
  .breadcrumb {
    position: absolute; left: 13px; top: 44px;
    font-size: 9.5px; color: var(--text-dark); display: flex; gap: 7px; align-items: center;
  }
  .breadcrumb .sep { color: #888; }
  .breadcrumb .current { color: var(--accent-red); }

  /* Sidebar */
  .side-menu {
    position: absolute; left: 137px; top: 261px; width: 214px;
    border-bottom: 2px solid #c3c3c3;
  }
  .side-menu li {
    list-style: none; height: 41px; padding-left: 14px; line-height: 41px;
    font-size: 11px; color: var(--text-dark);
    background: linear-gradient(#e9e9e9, var(--menu-grey));
    border-bottom: 1px solid #c8c8c8;
  }
  .promo {
    position: absolute; left: 137px; width: 214px; height: 144px;
    border: 2px solid #d4d4d4; overflow: hidden;
    background: linear-gradient(90deg, #f4f4f4 0%, #cfcfcf 45%, #7c7c7c 75%, #b5b5b5 100%);
  }
  .promo .promo-pct {
    position: absolute; left: 6px; top: 4px;
    font-size: 52px; font-weight: 500; color: var(--accent-red); line-height: 1;
  }
  .promo .promo-pct sup { font-size: 26px; vertical-align: top; }
  .promo .promo-flat {
    position: absolute; left: -24px; top: 82px; transform: rotate(-90deg);
    font-size: 48px; font-weight: 400; color: #9a9a9a; line-height: 1;
  }

  /* Article */
  .article { position: absolute; left: 374px; top: 264px; width: 517px; }
  .article h1 {
    font-size: 13px; font-weight: 400; color: var(--accent-red);
    padding-bottom: 6px; border-bottom: 1px solid var(--rule-grey);
  }
  .product-photo {
    float: left; width: 240px; height: 146px; margin: 15px 16px 6px 0;
    border: 2px solid #d6d6d6;
    background: radial-gradient(ellipse at center, #c8c8c8 0%, #f1f1f1 55%, #ffffff 100%);
  }
  .article p {
    font-size: 10.3px; line-height: 15.3px; text-align: justify; margin-top: 9px;
  }
  .article .lead { margin-top: 13px; }
  .btn-back {
    display: inline-block; margin-top: 12px; padding: 0 11px; height: 19px; line-height: 19px;
    background: #5a5a5a; color: var(--white); font-size: 9.5px;
  }

  /* Newsletter */
  .divider-line {
    position: absolute; left: 137px; top: 922px; width: 754px; height: 1px; background: #f0a5a5;
  }
  .newsletter {
    position: absolute; left: 137px; top: 941px; width: 240px; height: 38px;
    background: var(--soft-pink); display: flex; align-items: center; padding: 3px;
  }
  .newsletter .field {
    width: 175px; height: 32px; background: var(--white);
    display: flex; align-items: center; padding-left: 6px;
  }
  .newsletter .submit {
    flex: 1; text-align: center; font-size: 13px; font-weight: 700; color: #7a1b1b;
  }
  .newsletter-note {
    position: absolute; left: 397px; top: 939px; width: 494px;
    font-size: 10.3px; line-height: 15.3px; text-align: justify;
  }

  /* Footer */
  .site-footer {
    position: absolute; left: 0; top: 999px; width: 1028px; height: 173px;
    background: var(--footer-dark);
  }
  .footer-col { position: absolute; top: 20px; }
  .footer-col h3 { font-size: 9.5px; font-weight: 400; color: var(--accent-orange); text-transform: uppercase; }
  .footer-col p { margin-top: 17px; font-size: 8.7px; line-height: 17.5px; color: #d8d8d8; width: 100px; }
  .footer-sep {
    position: absolute; top: 22px; height: 140px; border-left: 1px dotted #5e5e5e;
  }
  .bottom-bar {
    position: absolute; left: 0; top: 1172px; width: 1028px; height: 28px;
    background: var(--bottom-bar); color: #cfcfcf; font-size: 8.5px;
    text-align: center; line-height: 28px;
  }
</style>
</head>
<body>

<header class="site-header">
  <div class="brand">Lumora</div>
  <div class="member-label">member of</div>
  <div class="partner-divider"></div>
  <div class="partner-badge" role="img" aria-label="Partner badge"></div>
  <nav class="utility-links">
    <a href="#">About Company</a><span>/</span><a href="#">Privacy Policy</a><span>/</span><a href="#">Contact</a>
  </nav>
  <div class="social">
    <i class="s-red" role="img" aria-label="Social network link"></i>
    <i class="s-blue" role="img" aria-label="Social network link"></i>
  </div>
</header>

<nav class="main-nav">
  <ul class="nav-links">
    <li>Optical Shops</li>
    <li>Discounts</li>
    <li>Goods</li>
    <li>Service</li>
  </ul>
  <a class="nav-cta cta-optician" href="#"><span class="cta-bg"></span><span class="cta-text">Meet Optician</span></a>
  <a class="nav-cta cta-shop" href="#"><span class="cta-bg"></span><span class="cta-text">Lumora Internet Shop
    <svg width="18" height="14" viewBox="0 0 18 14" aria-hidden="true">
      <path d="M1 2h3l2 8h9l2-6H5" fill="none" stroke="#fff" stroke-width="1.6"/>
      <circle cx="7" cy="12.5" r="1.3" fill="#fff"/><circle cx="14" cy="12.5" r="1.3" fill="#fff"/>
    </svg></span></a>
</nav>

<section class="category-panel">
  <h2>CATEGORIES</h2>
  <div class="breadcrumb">
    <span>Home</span><span class="sep">›</span><span>Product</span><span class="sep">›</span><span>Mockvane</span><span class="sep">›</span><span class="current">Featurez</span>
  </div>
</section>

<aside>
  <ul class="side-menu">
    <li>Optical Shops</li>
    <li>Discounts</li>
    <li>Goods</li>
    <li>Services</li>
  </ul>
  <div class="promo" style="top:442px" role="img" aria-label="Woman wearing sunglasses, black and white photo">
    <span class="promo-flat">Flat</span><span class="promo-pct">25<sup>%</sup></span>
  </div>
  <div class="promo" style="top:600px" role="img" aria-label="Woman wearing sunglasses, black and white photo">
    <span class="promo-flat">Flat</span><span class="promo-pct">25<sup>%</sup></span>
  </div>
  <div class="promo" style="top:757px" role="img" aria-label="Woman wearing sunglasses, black and white photo">
    <span class="promo-flat">Flat</span><span class="promo-pct">25<sup>%</sup></span>
  </div>
</aside>

<main class="article">
  <h1>Heading goes here</h1>
  <div class="product-photo" role="img" aria-label="Aviator sunglasses with dark gradient lenses"></div>
  <p class="lead">Lorem Ipsum is simply dummy text of the printing and typesetting industry. Lorem Ipsum has been the industry's standard dummy text ever since the 1500s, when an unknown printer took a galley of type and scrambled it to make a type specimen book.</p>
  <p>It has survived not only five centuries, but also the leap into electronic typesetting, remaining essentially unchanged. It was popularised in the 1960s with the release of Typeleaf sheets containing Lorem Ipsum passages, and more recently with desktop publishing software like Quarto PageForge including versions of Lorem Ipsum</p>
  <p>Lorem Ipsum is simply dummy text of the printing and typesetting industry. Lorem Ipsum has been the industry's standard dummy text ever since the 1500s, when an unknown printer took a galley of type and scrambled it to make a type specimen book.</p>
  <p>It has survived not only five centuries, but also the leap into electronic typesetting, remaining essentially unchanged. It was popularised in the 1960s with the release of Typeleaf sheets containing Lorem Ipsum passages, and more recently with desktop publishing software like Quarto PageForge including versions of Lorem Ipsum</p>
  <p>Lorem Ipsum is simply dummy text of the printing and typesetting industry. Lorem Ipsum has been the industry's standard dummy text ever since the 1500s, when an unknown printer took a galley of type and scrambled it to make a type specimen book.</p>
  <p>It has survived not only five centuries, but also the leap into electronic typesetting, remaining essentially unchanged. It was popularised in the 1960s with the release of Typeleaf sheets containing Lorem Ipsum passages, and more recently with desktop publishing software like Quarto PageForge including versions of.</p>
  <a class="btn-back" href="#">Back</a>
</main>

<div class="divider-line"></div>
<form class="newsletter">
  <div class="field">
    <svg width="20" height="14" viewBox="0 0 20 14" aria-hidden="true">
      <rect x="0.5" y="0.5" width="19" height="13" fill="#f6a3a3" stroke="#ef7f7f"/>
      <path d="M1 1l9 7 9-7" fill="none" stroke="#e35f5f" stroke-width="1.2"/>
    </svg>
  </div>
  <span class="submit">SUBMIT</span>
</form>
<p class="newsletter-note">Lorem Ipsum is simply dummy text of the printing and typesetting industry. Lorem Ipsum has been the industry's standard dummy text ever since the 1500s, when an unknown printer took a galley of type and scrambled it to make a type specimen book.</p>

<footer class="site-footer">
  <div class="footer-col" style="left:151px"><h3>Quick Link</h3><p>Lorem Ipsum has been the industry's standard dummy text Lorem Ipsum has been the industry's standard dummy text</p></div>
  <div class="footer-sep" style="left:280px"></div>
  <div class="footer-col" style="left:309px"><h3>Goods</h3><p>Lorem Ipsum has been the industry's standard dummy text Lorem Ipsum has been the industry's standard dummy text</p></div>
  <div class="footer-sep" style="left:441px"></div>
  <div class="footer-col" style="left:474px"><h3>Services</h3><p>Lorem Ipsum has been the industry's standard dummy text Lorem Ipsum has been the industry's standard dummy text</p></div>
  <div class="footer-sep" style="left:592px"></div>
  <div class="footer-col" style="left:622px"><h3>Lences</h3><p>Lorem Ipsum has been the industry's standard dummy text Lorem Ipsum has been the industry's standard dummy text</p></div>
  <div class="footer-sep" style="left:744px"></div>
  <div class="footer-col" style="left:773px"><h3>Information</h3><p>Lorem Ipsum has been the industry's standard dummy text Lorem Ipsum has been the industry's standard dummy text</p></div>
</footer>
<div class="bottom-bar">Design © 2014. All Rights Reserved.</div>

</body>
</html>
```